Consulting company needs Business Cards - rough concept provided

I'm looking for someone to take our business card idea and make is slick and polished - to communicate our high-end, sophisticated, serious consulting business. We have a rough layout we did in-house. We are open to ideas on repo-ing elements, adjusting sizes, typefaces etc... within the general concept we've already come up with. We want it to be super-clean and sophisticated. We want to keep the white backgrounds, and blue brand colors. Our goal is to print with painted blue edges on thick cardstock. Thank you!!

```html
<!DOCTYPE html>
<html lang="en">
<head>
<meta charset="utf-8">
<title>Northvale Business Cards</title>
<link href="https://fonts.googleapis.com/css2?family=Arimo:wght@400;700&display=swap" rel="stylesheet">
<style>
  :root {
    --backdrop: #e4e4e2;
    --card-white: #ffffff;
    --brand-navy: #0b3e6b;
    --brand-blue: #1f78b4;
    --card-navy: #0d3f6e;
    --text-grey: #9a9fa5;
    --text-dark: #1e2a36;
    --text-light: #d9e4ee;
    --name-cream: #ece6d6;
  }
  * { box-sizing: border-box; margin: 0; padding: 0; }
  html, body {
    width: 1200px; height: 703px; overflow: hidden;
    background: var(--backdrop);
    font-family: "Arimo", Arial, sans-serif;
  }
  .canvas {
    position: relative; width: 1200px; height: 703px;
    display: flex; align-items: center; justify-content: center; gap: 60px;
  }
  .card {
    position: relative; width: 525px; height: 300px;
    border-radius: 4px; overflow: hidden;
    box-shadow: 0 2px 6px rgba(0,0,0,0.12);
  }
  .card--front { background: var(--card-white); }
  .card--back { background: var(--card-navy); }

  .wordmark {
    position: absolute; top: 22px; left: 28px; right: 28px;
    font-weight: 700; font-size: 64px; letter-spacing: 1px; line-height: 1;
    text-align: right;
  }
  .card--front .wordmark { color: var(--brand-navy); }
  .card--back .wordmark { color: var(--brand-blue); }

  .mission {
    position: absolute; left: 30px; top: 118px; width: 300px;
    font-size: 21px; line-height: 1.42; color: var(--text-grey);
  }
  .mission strong { color: var(--brand-navy); font-weight: 700; }

  .contact {
    position: absolute; font-size: 11px; line-height: 1.5;
  }
  .card--front .contact { right: 30px; top: 122px; color: var(--text-dark); font-weight: 700; }
  .card--back .contact { left: 32px; top: 196px; font-size: 15px; color: var(--text-light); line-height: 1.45; }

  .person {
    position: absolute; left: 32px; top: 130px;
  }
  .person__name { font-size: 21px; font-weight: 700; letter-spacing: 0.5px; }
  .person__first { color: var(--brand-blue); }
  .person__last { color: var(--name-cream); }
  .person__role {
    font-size: 20px; color: var(--text-light); letter-spacing: 0.5px; margin-top: 3px;
  }
</style>
</head>
<body>
<main class="canvas">
  <section class="card card--front" aria-label="Card front">
    <div class="wordmark">NORTHVALE</div>
    <p class="mission">
      <strong>We help</strong> [target demographic] <strong>achieve</strong>
      [desired emotional outcome] <strong>by</strong> [our unique approach]
      <strong>because</strong> [our brand beliefs]
    </p>
    <address class="contact" style="font-style:normal">
      4820 Larchmont Ave, Ste 210<br>
      Fairview, OR 97024<br>
      (503) 555 0187<br>
      info@northvale.com
    </address>
  </section>

  <section class="card card--back" aria-label="Card back">
    <div class="wordmark">NORTHVALE</div>
    <div class="person">
      <div class="person__name"><span class="person__first">DANA</span> <span class="person__last">WHITLOCK</span></div>
      <div class="person__role">BRAND CONSULTANT</div>
    </div>
    <address class="contact" style="font-style:normal">
      4820 Larchmont Ave, Ste 210<br>
      Fairview, OR 97024<br>
      (503) 555 0187<br>
      dana@northvale.com
    </address>
  </section>
</main>
</body>
</html>
```